Business Card for TKR, logo files already created

Please, can you assist with creating a Business card the TKR graphics which are already listed on www.tarnkeyrelay.example
The business card should be modern and upmarket, textured designs are welcome. Please feel free to express yourself and be very bold with your design.

Target Market(s)

Cyber Security

Industry/Entity Type

Information Technology

Contact Information for Business Card

Company Name
Name
Title
Mobile
Fax or Tel
email
url

Font styles to use
Serif
Sans Serif

Colors
3277b5
85acd3
ffffff

```html
<!DOCTYPE html>
<html lang="en">
<head>
<meta charset="utf-8">
<title>TKR Business Card</title>
<link rel="stylesheet" href="https://fonts.googleapis.com/css2?family=Exo+2:wght@700;800&family=Open+Sans:wght@400;600&display=swap">
<style>
  :root {
    --navy: #263a80;
    --navy-deep: #1f3070;
    --graphite: #4a4a4c;
    --white: #ffffff;
    --paper: #ffffff;
    --backdrop: #e9e6e1;
    --ink-soft: #2c3c7a;
  }
  * { margin: 0; padding: 0; box-sizing: border-box; }
  html, body { width: 1200px; height: 1200px; overflow: hidden; }
  body {
    background: var(--backdrop);
    font-family: "Open Sans", Arial, sans-serif;
    position: relative;
  }
  .card {
    position: absolute;
    left: 180px;
    width: 840px;
    height: 480px;
    overflow: hidden;
    box-shadow: 0 10px 28px rgba(0,0,0,0.18);
  }

  /* Front */
  .card-front { top: 80px; background: var(--navy); color: var(--white); }
  .front-brand {
    position: absolute; left: 0; right: 0; top: 120px;
    text-align: center;
  }
  .brand-mark {
    font-family: "Exo 2", Arial, sans-serif;
    font-weight: 800;
    font-size: 150px;
    line-height: 1;
    letter-spacing: 4px;
  }
  .brand-name {
    font-family: "Exo 2", Arial, sans-serif;
    font-weight: 800;
    font-size: 40px;
    letter-spacing: 6px;
    margin-top: 6px;
  }
  .tagline {
    display: flex; align-items: center; justify-content: center; gap: 16px;
    margin-top: 14px;
    font-size: 18px; letter-spacing: 3px; text-transform: uppercase;
  }
  .tagline .rule { width: 90px; height: 2px; background: currentColor; }

  /* Back */
  .card-back { top: 640px; background: var(--paper); color: var(--navy); }
  .back-brand {
    position: absolute; right: 56px; top: 40px; text-align: right;
  }
  .back-brand .brand-mark { font-size: 92px; color: var(--navy); }
  .back-brand .brand-name { font-size: 26px; letter-spacing: 4px; color: var(--navy); margin-top: 2px; }
  .back-brand .tagline { justify-content: flex-end; font-size: 13px; letter-spacing: 2px; margin-top: 8px; }
  .back-brand .tagline .rule { width: 50px; height: 1.5px; }
  .divider {
    position: absolute; left: 56px; right: 56px; top: 252px;
    height: 1.5px; background: var(--navy);
  }
  .contact {
    position: absolute; left: 56px; top: 272px;
  }
  .person-name {
    font-weight: 600; font-size: 36px; letter-spacing: 1px; text-transform: uppercase;
    line-height: 1.1;
  }
  .person-title { font-size: 16px; text-transform: uppercase; letter-spacing: 1px; color: var(--ink-soft); margin-bottom: 10px; }
  .contact-list { list-style: none; }
  .contact-list li {
    display: flex; align-items: center; gap: 12px;
    font-size: 17px; color: #333a55; line-height: 1.5;
  }
  .contact-list svg { width: 16px; height: 16px; fill: var(--navy); flex: none; }
  .footer-band {
    position: absolute; left: 0; right: 0; bottom: 0; height: 22px; display: flex;
  }
  .footer-band .band-navy { flex: 0 0 62%; background: var(--navy); }
  .footer-band .band-graphite { flex: 1; background: var(--graphite); }
</style>
</head>
<body>
  <section class="card card-front">
    <div class="front-brand">
      <div class="brand-mark">TKR</div>
      <div class="brand-name">TARNKEY RELAY</div>
      <div class="tagline"><span class="rule"></span>Intelligence - Driven Solutions<span class="rule"></span></div>
    </div>
  </section>

  <section class="card card-back">
    <div class="back-brand">
      <div class="brand-mark">TKR</div>
      <div class="brand-name">TARNKEY RELAY</div>
      <div class="tagline"><span class="rule"></span>Intelligence - Driven Solutions</div>
    </div>
    <div class="divider"></div>
    <div class="contact">
      <div class="person-name">Daniel Orwen</div>
      <div class="person-title">Manager &amp; CEO</div>
      <ul class="contact-list">
        <li><svg viewBox="0 0 16 16"><path d="M3.5 1.5l2.5 0 1 3.5-1.8 1.2a8 8 0 0 0 4.6 4.6l1.2-1.8 3.5 1v2.5c0 .8-.7 1.5-1.5 1.5A12 12 0 0 1 2 3c0-.8.7-1.5 1.5-1.5z"/></svg>+100-555-0142</li>
        <li><svg viewBox="0 0 16 16"><path d="M2 5h12v9H2zM4 1h6v3H4zM4 7h2v2H4zm3 0h2v2H7zm3 0h2v2h-2zM4 10h2v2H4zm3 0h2v2H7zm3 0h2v2h-2z"/></svg>+100-555-0187</li>
        <li><svg viewBox="0 0 16 16"><path d="M1 3h14v10H1zm1.5 1.3V12h11V4.3L8 8.5z"/></svg>contact@tarnkeyrelay.example</li>
        <li><svg viewBox="0 0 16 16"><circle cx="8" cy="8" r="6.5" fill="none" stroke="#263a80" stroke-width="1.5"/><path d="M1.5 8h13M8 1.5c-3 3.5-3 9.5 0 13M8 1.5c3 3.5 3 9.5 0 13" fill="none" stroke="#263a80" stroke-width="1.2"/></svg>www.tarnkeyrelay.example</li>
      </ul>
    </div>
    <div class="footer-band"><span class="band-navy"></span><span class="band-graphite"></span></div>
  </section>
</body>
</html>
```